Business Card Design Project

We need a buisness card for a new digital sinage company. Our target cliants are small to mediaum buisness who want to advertise on out digital sinage network

Target Market(s)

Small to medium buisness

Industry/Entity Type

Digital

Requirements
Must have
• Must have logo

```html
<!DOCTYPE html>
<html lang="en">
<head>
<meta charset="utf-8">
<title>Lumo Business Card</title>
<link href="https://fonts.googleapis.com/css2?family=Nunito:wght@300;400;800&display=swap" rel="stylesheet">
<style>
  :root {
    --bg: #e9e6e1;
    --blue-light: #2f8cb6;
    --blue-dark: #175876;
    --white-card: #f4f4f4;
    --white-card-edge: #dcdcdc;
    --ink-grey: #4a4a4a;
    --soft-grey: #8c8c8c;
    --on-blue: #ffffff;
    --on-blue-soft: rgba(255,255,255,0.75);
    --accent-blue: #4aa3d8;
    --accent-green: #7cc36a;
  }
  * { box-sizing: border-box; margin: 0; padding: 0; }
  html, body { width: 1200px; height: 801px; overflow: hidden; }
  body {
    background: var(--bg);
    font-family: "Nunito", sans-serif;
    display: flex;
    align-items: center;
    justify-content: center;
    gap: 70px;
  }
  .card {
    width: 500px;
    height: 290px;
    border-radius: 6px;
    position: relative;
    overflow: hidden;
    box-shadow: 0 10px 28px rgba(0,0,0,0.18);
  }
  /* Front: blue contact side */
  .card--front {
    background: linear-gradient(135deg, var(--blue-light), var(--blue-dark));
    color: var(--on-blue);
  }
  .card--front .watermark-name {
    position: absolute;
    right: 28px;
    top: 22px;
    font-weight: 800;
    font-size: 96px;
    line-height: 1;
    color: rgba(255,255,255,0.14);
  }
  .card--front .brand {
    position: absolute;
    left: 36px;
    top: 120px;
    font-weight: 800;
    font-size: 34px;
    line-height: 1;
  }
  .card--front .person {
    position: absolute;
    left: 36px;
    top: 168px;
  }
  .person__name { font-weight: 300; font-size: 24px; line-height: 1.1; }
  .person__role { font-weight: 300; font-size: 11px; color: var(--on-blue-soft); margin-top: 4px; line-height: 1.4; }
  .contact {
    position: absolute;
    right: 32px;
    bottom: 32px;
    list-style: none;
    font-weight: 300;
    font-size: 13px;
    color: var(--on-blue-soft);
  }
  .contact li { display: flex; align-items: center; gap: 10px; margin-top: 8px; }
  .contact .icon { width: 12px; height: 12px; flex: none; }
  .contact .icon--mail { background: var(--accent-green); }
  /* Back: white brand side */
  .card--back {
    background: linear-gradient(160deg, #ffffff, var(--white-card) 60%, var(--white-card-edge));
    display: flex;
    flex-direction: column;
    align-items: center;
    justify-content: center;
  }
  .brand-lockup { display: flex; align-items: center; gap: 14px; }
  .brand-lockup__square { width: 34px; height: 34px; background: var(--accent-blue); border-radius: 4px; }
  .brand-lockup__name { font-weight: 800; font-size: 76px; line-height: 1; color: var(--ink-grey); }
  .card--back .website { margin-top: 12px; font-weight: 300; font-size: 16px; color: var(--soft-grey); letter-spacing: 0.5px; }
</style>
</head>
<body>
  <section class="card card--front" aria-label="Card front">
    <div class="watermark-name" aria-hidden="true">Lumo</div>
    <div class="brand">Lumo</div>
    <div class="person">
      <p class="person__name">Nadia Rowell</p>
      <p class="person__role">Sales Director<br>Perth, WA</p>
    </div>
    <ul class="contact">
      <li>
        <svg class="icon" viewBox="0 0 12 12" aria-hidden="true"><path d="M2.5 1 L4.5 1 L5.2 3.3 L4 4.3 Q5 6.8 7.7 8 L8.7 6.8 L11 7.5 L11 9.5 Q10.5 11 9 11 Q1 10 1 2.8 Q1 1.3 2.5 1 Z" fill="rgba(255,255,255,0.75)"/></svg>
        <span>0400 123 456</span>
      </li>
      <li>
        <span class="icon icon--mail" aria-hidden="true"></span>
        <span>nadia@lumo.com.au</span>
      </li>
    </ul>
  </section>

  <section class="card card--back" aria-label="Card back">
    <div class="brand-lockup">
      <span class="brand-lockup__square" aria-hidden="true"></span>
      <span class="brand-lockup__name">Lumo</span>
    </div>
    <p class="website">www.lumo.com.au</p>
  </section>
</body>
</html>
```